We would like a business card that includes our logo on the front and the following information on the back:

Warren Pike, Owner
Phone: (555) 614-0827
email: wpikefencing@brookmail.example

Wally Pike & Sons Fencing provides the following services:
Barbed wire
Smooth wire
High tensile
Electric

On the bottom of the card please add:
Please call or email Warren for estimates.

```html
<!DOCTYPE html>
<html lang="en">
<head>
<meta charset="utf-8">
<title>Wally Pike &amp; Sons Fencing – Business Card</title>
<link rel="stylesheet" href="https://fonts.googleapis.com/css2?family=Arimo:ital,wght@0,400;0,700;1,400&family=Ultra&display=swap">
<style>
  :root {
    --page: #e4e2df;
    --card-light: #ffffff;
    --card-dark: #2c2523;
    --brown: #7b563b;
    --brown-deep: #5e4130;
    --ink: #3a3a3a;
    --cream: #f4efe9;
  }
  * { box-sizing: border-box; margin: 0; padding: 0; }
  html, body {
    width: 1200px; height: 718px; overflow: hidden;
    background: var(--page);
  }
  .sheet {
    position: relative; width: 1200px; height: 718px;
    display: flex; align-items: center; justify-content: center; gap: 30px;
  }
  .card {
    position: relative; width: 560px; height: 320px;
    border-radius: 18px; overflow: hidden;
    box-shadow: 0 6px 18px rgba(0,0,0,0.18);
  }

  /* Back: contact details */
  .card--details { background: var(--card-light); color: var(--ink); }
  .details { position: absolute; left: 40px; top: 34px; z-index: 2; }
  .details__name {
    font-family: "Ultra", "Rockwell Extra Bold", "Rockwell", "Roboto Slab", "DejaVu Serif", serif;
    font-weight: 400; font-synthesis: none;
    font-size: 30px; letter-spacing: 1px; color: var(--brown);
    line-height: 1;
  }
  .details__role { font-family: "Arimo", sans-serif; font-size: 14px; margin-top: 8px; }
  .contact { margin-top: 12px; font-family: "Arimo", sans-serif; }
  .contact__row { display: flex; align-items: center; gap: 8px; }
  .contact__row svg { width: 13px; height: 13px; fill: var(--brown); flex: none; }
  .contact__phone { font-size: 19px; font-weight: 700; }
  .contact__email { font-size: 13px; margin-top: 3px; }
  .services { list-style: none; margin-top: 16px; margin-left: 14px; font-family: "Arimo", sans-serif; font-size: 16px; }
  .services li { display: flex; align-items: center; gap: 10px; line-height: 24px; }
  .services svg { width: 14px; height: 14px; flex: none; }
  .estimate { margin-top: 14px; margin-left: 28px; font-family: "Arimo", sans-serif; font-size: 15px; line-height: 1.2; }
  .estimate em { display: block; font-size: 13px; }
  .fence-art--light {
    position: absolute; right: 0; bottom: 0; width: 240px; height: 210px;
    background: linear-gradient(160deg, rgba(123,86,59,0) 0%, rgba(123,86,59,0.55) 35%, var(--brown) 100%);
  }

  /* Front: company name */
  .card--brand { background: var(--card-dark); }
  .fence-art--dark {
    position: absolute; left: 0; top: 0; width: 330px; height: 100%;
    background: linear-gradient(110deg, var(--brown-deep) 0%, var(--brown) 55%, rgba(123,86,59,0.2) 100%);
  }
  .brand {
    position: absolute; right: 28px; top: 190px; width: 190px;
    font-family: "Arimo", sans-serif; font-weight: 400; font-size: 17px;
    line-height: 1.3; color: var(--cream); text-align: center;
  }
</style>
</head>
<body>
<main class="sheet">

  <section class="card card--details" aria-label="Card back with contact details">
    <div class="details">
      <h1 class="details__name">WARREN PIKE</h1>
      <p class="details__role">Owner</p>
      <div class="contact">
        <p class="contact__row contact__phone">
          <svg viewBox="0 0 24 24" aria-hidden="true"><path d="M6.6 10.8a15.1 15.1 0 0 0 6.6 6.6l2.2-2.2c.3-.3.7-.4 1-.2 1.1.4 2.3.6 3.6.6.6 0 1 .4 1 1V20c0 .6-.4 1-1 1A17 17 0 0 1 3 4c0-.6.4-1 1-1h3.5c.6 0 1 .4 1 1 0 1.3.2 2.5.6 3.6.1.3 0 .7-.2 1z"/></svg>
          (555) 614-0827
        </p>
        <p class="contact__row contact__email">
          <svg viewBox="0 0 24 24" aria-hidden="true"><path d="M2 5h20v14H2z M2 5l10 8 10-8" stroke="#fff" stroke-width="1.5"/></svg>
          wpikefencing@brookmail.example
        </p>
      </div>
      <ul class="services">
        <li><svg viewBox="0 0 16 16" aria-hidden="true"><circle cx="8" cy="8" r="8" fill="#7b563b"/><path d="M4.5 8.2l2.3 2.3 4.7-4.8" fill="none" stroke="#fff" stroke-width="1.8"/></svg>Barbed wire</li>
        <li><svg viewBox="0 0 16 16" aria-hidden="true"><circle cx="8" cy="8" r="8" fill="#7b563b"/><path d="M4.5 8.2l2.3 2.3 4.7-4.8" fill="none" stroke="#fff" stroke-width="1.8"/></svg>Smooth wire</li>
        <li><svg viewBox="0 0 16 16" aria-hidden="true"><circle cx="8" cy="8" r="8" fill="#7b563b"/><path d="M4.5 8.2l2.3 2.3 4.7-4.8" fill="none" stroke="#fff" stroke-width="1.8"/></svg>High tensile</li>
        <li><svg viewBox="0 0 16 16" aria-hidden="true"><circle cx="8" cy="8" r="8" fill="#7b563b"/><path d="M4.5 8.2l2.3 2.3 4.7-4.8" fill="none" stroke="#fff" stroke-width="1.8"/></svg>Electric</li>
      </ul>
      <p class="estimate"><em>Please call or email</em>Warren for estimates.</p>
    </div>
    <div class="fence-art fence-art--light" role="img" aria-label="Illustration of a wooden fence post with barbed wire strands"></div>
  </section>

  <section class="card card--brand" aria-label="Card front with company name">
    <div class="fence-art fence-art--dark" role="img" aria-label="Large illustration of a wooden fence post and rails wrapped in barbed wire"></div>
    <p class="brand">Wally Pike &amp; Sons Fencing</p>
  </section>

</main>
</body>
</html>
```